Doctors Office Web Design

Name of the business is Lian-Hua Qiu M.D.
We need a web design that is attractive for women that want to see Dr. Lian-Hua Qiu for Obstetrician Gynecology and Pregnancy care. Dr. Qiu earned her degree from Harbor Crest Medical College of obstetrician gynecology. We want to attract women of child bearing ages to come to our offices for health, education, and pregnancies.

Please visit http://www.drqiucare-example.com/ to help you get a feel for who we are. We will be adding some pictures and logo in the next few days.

We are looking for to have pages for and tabs including
About Us- History, Our Staff, Dr. Qiu
Patient Information- Appointments, E-Prescriptions, Payments Accepted, Insurance
Health- General, Sexual, Mental, Affiliates
Pregnancy- Minimally invasive surgery(our specialty), 4-D Ultra Sound, Hospital Affiliations
Media- News,Pictures, Videos
Locations- Palmvale Office, Marlow Office

The colors we would like to use are pastel colors, magenta, and plum

Target Market(s)

Women of all ages with an emphasis on 25-65 year olds

Industry/Entity Type

Business

Requirements
Must have
• Needs to include a location for a our videos and pictures that I will submit shortly. We also want a map to our location or atleast a place for one.
Nice to have
• A place for a google map of our office locations.

```html
<!DOCTYPE html>
<html lang="en">
<head>
<meta charset="utf-8">
<title>Lian-Hua Qiu M.D.</title>
<link rel="stylesheet" href="https://fonts.googleapis.com/css2?family=Noto+Serif:wght@400&family=Ubuntu:wght@400;500;700&family=Open+Sans:wght@400;600&display=swap">
<style>
:root{
  --plum:#8c0c70;
  --plum-dark:#6e0a58;
  --magenta:#d41a92;
  --magenta-soft:#e93ca8;
  --pink-pale:#fdf0f8;
  --pink-line:#f1c9e3;
  --text:#555;
  --heading:#3a3a3a;
  --white:#fff;
}
*{box-sizing:border-box;margin:0;padding:0}
html,body{width:1050px;height:1200px;overflow:hidden}
body{position:relative;font-family:"Open Sans",Arial,sans-serif;color:var(--text);
  background:linear-gradient(#e9e9e9 0,#f6f6f6 230px,#fff 230px,#fff 923px,#d92c9b 923px,#a31a80 1200px);}
.abs{position:absolute}
.top-line{left:0;top:0;width:1050px;height:3px;background:var(--magenta)}
.util-nav{left:791px;top:0;width:167px;height:24px;background:linear-gradient(var(--magenta),#b5107b);border-radius:0 0 6px 6px;
  color:#fff;font:11px "Ubuntu",sans-serif;display:flex;align-items:center;justify-content:center;gap:5px}
.brand{left:97px;top:33px;font:28px "Noto Serif",serif;color:var(--plum);letter-spacing:.2px}
.search{left:795px;top:32px;width:163px;height:22px;display:flex;border-radius:11px;overflow:hidden;border:1px solid #ddd}
.search-field{flex:1;background:#fff;font-size:10px;color:#aaa;padding:5px 12px}
.search-go{width:34px;background:var(--plum);color:#fff;font:10px "Ubuntu",sans-serif;display:flex;align-items:center;justify-content:center}
.main-nav{left:111px;top:93px;display:flex;gap:3.5px}
.main-nav a{height:25px;background:linear-gradient(#9a1480,var(--plum-dark));color:#fff;border-radius:7px 7px 0 0;
  font:500 11.5px "Ubuntu",sans-serif;display:flex;align-items:center;justify-content:center;text-decoration:none}
.follow{left:754px;top:94px;display:flex;align-items:center;gap:4px;font:15px "Ubuntu",sans-serif;color:#666}
.follow span.sq{width:22px;height:22px;border-radius:4px;background:var(--plum)}
.follow .label{margin-right:6px}
.hero{left:94px;top:118px;width:859px;height:293px;border:3px solid var(--plum);border-radius:8px;background:var(--plum);overflow:hidden}
.hero-photo{left:0;top:0;width:562px;height:287px;background:linear-gradient(100deg,#f4f8fb,#cde0ef 45%,#e9eef2)}
.hero-copy{left:572px;top:6px;width:270px;color:#fff}
.hero-copy h1{font:400 22px/26px "Ubuntu",sans-serif;letter-spacing:1px}
.hero-copy h1 b{font-weight:700;font-size:24px}
.hero-copy p{margin-top:10px;padding-top:8px;border-top:1px solid rgba(255,255,255,.25);font-size:9.6px;line-height:17.5px;letter-spacing:.7px;text-align:justify}
.btn-light{left:578px;top:213px;width:89px;height:26px;border-radius:13px;background:linear-gradient(#fff,#ddd);color:#777;
  font:700 13px "Ubuntu",sans-serif;display:flex;align-items:center;justify-content:center}
.dots{left:704px;top:266px;display:flex;gap:11px}
.dots i{width:14px;height:14px;border-radius:50%;background:var(--magenta)}
.dots i.on{background:var(--plum-dark);border:2px solid var(--magenta)}
.content{left:94px;top:414px;width:859px;height:588px;background:#fff;border-radius:0 0 8px 8px}
.feature{width:196px;top:429px}
.feature h2{display:flex;align-items:center;gap:6px;font:500 15.5px "Ubuntu",sans-serif;color:var(--heading);height:28px}
.feature .ico{width:26px;height:26px;border-radius:5px}
.frame{margin-top:6px;height:73px;border:1px solid #ccc;padding:4px;background:#fff}
.frame div{height:100%}
.feature p{margin-top:10px;font-size:9.6px;line-height:15.75px;text-align:justify}
.feature ul{list-style:none;font-size:9.6px;line-height:15.75px}
.feature li{padding-left:16px;position:relative}
.feature li:before,.arrow-list li:before{content:"";position:absolute;left:4px;top:5px;border:3.5px solid transparent;border-left:4px solid var(--plum)}
.sep{top:432px;width:0;height:250px;border-left:1px dotted #ccc}
.btn{height:17px;border-radius:9px;background:linear-gradient(var(--magenta-soft),var(--plum));color:#fff;font-size:10px;
  display:flex;align-items:center;justify-content:center;box-shadow:0 1px 2px rgba(0,0,0,.3)}
.shadow-rule{left:94px;top:692px;width:859px;height:8px;background:linear-gradient(#f3f3f3,#fff)}
.office{left:96px;top:720px;width:562px;height:264px;background:var(--pink-pale);border:1px solid var(--pink-line);border-radius:8px}
.map{left:106px;top:733px;width:316px;height:242px;border:4px solid #fff;box-shadow:0 0 0 1px #ddd;
  background:linear-gradient(135deg,#efe9df,#f5efe2 50%,#e6e0d4)}
.office-copy{left:432px;top:741px;width:211px}
.office-copy h2{font:400 19px "Ubuntu",sans-serif;color:#555;margin-left:3px}
.office-copy h2 span{color:var(--plum)}
.office-copy p{margin-top:6px;font-size:9.6px;line-height:17.5px;text-align:justify;color:#444}
.btn-dark{left:555px;top:947px;width:91px;height:20px;border-radius:10px;background:linear-gradient(#555,#222);color:#fff;
  font:12px "Ubuntu",sans-serif;display:flex;align-items:center;justify-content:center}
.services{left:685px;top:719px;width:268px}
.services h2{font:500 19px "Ubuntu",sans-serif;color:#666;letter-spacing:1px;margin-left:4px}
.services h2 span{color:var(--plum)}
.arrow-list{list-style:none;margin-top:10px;font-size:9.6px;line-height:21px;color:#444;white-space:nowrap}
.arrow-list li{position:relative;padding-left:12px}
.arrow-list li:before{left:0;top:7px}
.footer-col{color:#fff}
.footer-col h3{font:400 19px "Ubuntu",sans-serif}
.footer-col ul{list-style:none;margin-top:5px;font-size:10.5px;line-height:14px;letter-spacing:.8px}
.footer-col li{position:relative;padding-left:13px}
.footer-col li:before{content:"";position:absolute;left:0;top:3px;border:3.5px solid transparent;border-left:4px solid #fff}
.footer-col p{margin-top:6px;font-size:10px;line-height:16px;letter-spacing:.5px;text-align:justify}
.contact-cols{display:flex}
.contact-cols p{text-align:left;white-space:nowrap}
.contact-cols p:first-child{width:179px}
.vrule{top:1025px;height:128px;border-left:1px dotted rgba(255,255,255,.5)}
.badge{left:849px;top:1018px;width:96px;height:122px;background:#fff;border:1px solid #ddd}
.badge i{position:absolute;left:30px;top:14px;width:36px;height:48px;border-radius:50%;background:#f0d4e6}
.legal{top:1181px;color:#fff;font-size:10.5px;letter-spacing:.3px}
</style>
</head>
<body>
<div class="abs top-line"></div>
<nav class="abs util-nav"><span>Home</span><span>/</span><span>Register</span><span>/</span><span>Sitemap</span></nav>
<div class="abs brand">Lian-Hua Qiu M.D.</div>
<div class="abs search"><div class="search-field">Search</div><div class="search-go">GO</div></div>

<nav class="abs main-nav">
  <a style="width:76px">About Us</a>
  <a style="width:115px">Patient Information</a>
  <a style="width:57px">Health</a>
  <a style="width:71px">Pregnancy</a>
  <a style="width:58px">Media</a>
  <a style="width:73px">Locations</a>
</nav>
<div class="abs follow"><span class="label">Follow us on</span><span class="sq"></span><span class="sq"></span><span class="sq"></span><span class="sq"></span></div>

<section class="abs hero">
  <div class="abs hero-photo" role="img" aria-label="Photo of smiling doctors and nurses in white coats and scrubs"></div>
  <div class="abs hero-copy">
    <h1>Serving All Areas of<br><b>Women's Health,</b><br>Including:</h1>
    <p>Welcome to Dr. Lian-Hua Qiu's website. Here you will be able to find information about both of our offices, meet Dr. Qiu and her staff, and browse through our women's health links to learn more about pregnancy, nutrition, exercise, and other women's health issues.</p>
  </div>
  <div class="abs btn-light">More info</div>
  <div class="abs dots"><i></i><i></i><i></i><i></i><i class="on"></i><i></i></div>
</section>

<div class="abs content"></div>

<article class="abs feature" style="left:103px">
  <h2><span class="ico" role="img" aria-label="Tools icon" style="background:linear-gradient(#ccc,#888)"></span>About the Practice</h2>
  <div class="frame"><div role="img" aria-label="Photo of the medical team" style="background:linear-gradient(#c9d9e6,#eef2f4)"></div></div>
  <p>All about Lian-Hua Qiu, M.D., P.A. Includes addresses, directions, contact numbers, office hours,<br><br>Dr. Qiu's hospital affiliations, and insur-ance plans accepted.Dr. Qiu's hospital affiliations, and insurance</p>
</article>
<div class="abs sep" style="left:307px"></div>
<article class="abs feature" style="left:316px">
  <h2><span class="ico" role="img" aria-label="Doctor icon" style="background:linear-gradient(#e8c08c,#6a4a2a)"></span>Meet Dr. Qiu</h2>
  <div class="frame"><div role="img" aria-label="Photo of Dr. Qiu in her office" style="background:linear-gradient(90deg,#3a1c1c,#d8d0cc 50%,#4a2020)"></div></div>
  <p>Dr. Qiu's goal is to provide current and compassionate women's healthcare in a fashion that acknowledges her patients' diverse values, backgrounds, and condi-tions. Dr. Qiu acknowledges the whole individual and recognizes the inseparability of the body.</p>
</article>
<div class="abs sep" style="left:522px"></div>
<article class="abs feature" style="left:532px">
  <h2><span class="ico" role="img" aria-label="Medical kit icon" style="background:linear-gradient(#e04a3a,#9ac6d8)"></span>Women's Health Info</h2>
  <div class="frame"><div role="img" aria-label="Photo of a woman running at dawn" style="background:linear-gradient(#1e4a7a,#7da6c8 70%,#8a8a80)"></div></div>
  <p>(GYN) Get answers to your gynecologic and women's health concerns by following links to academic articles, medical sites, and to special.<br><br>medical sites, and to special information that Dr. Qiu provides to her patients.</p>
</article>
<div class="abs sep" style="left:737px"></div>
<article class="abs feature" style="left:746px">
  <h2><span class="ico" role="img" aria-label="Mother and child icon" style="background:linear-gradient(#9ab08a,#4a6a4a)"></span>The Pregnancy</h2>
  <div class="frame"><div role="img" aria-label="Photo of a group of young women" style="background:linear-gradient(90deg,#f3e6dc,#e8b89a 50%,#f1e4da)"></div></div>
  <p style="margin-bottom:0">Where can I find more information about</p>
  <ul><li>pregnancy?</li><li>Preconceptional Care</li><li>Pregnancy Testing</li><li>Pregnancy Health</li><li>High Risk Pregnancy</li><li>Pregnancy Loss</li></ul>
</article>

<div class="abs btn" style="left:230px;top:668px;width:60px">more info</div>
<div class="abs btn" style="left:449px;top:668px;width:60px">more info</div>
<div class="abs btn" style="left:668px;top:668px;width:60px">more info</div>
<div class="abs btn" style="left:888px;top:668px;width:60px">more info</div>

<div class="abs shadow-rule"></div>

<section class="abs office"></section>
<div class="abs map" role="img" aria-label="Street map showing the office location"></div>
<div class="abs office-copy">
  <h2>Office<span>Location</span></h2>
  <p>Dr. Qiu serves her patients in two different offices. On Mondays, Tuesdays and Thursdays, Dr. Qiu sees patients in her Marlow office, and on Wednesdays and Fridays, she sees patients in Palmvale. Please call either number for an appointment. Pharmacies can also fax requests via Dr. Qiu's fax number at her Marlow office.</p>
</div>
<div class="abs btn-dark">View Full Map</div>

<section class="abs services">
  <h2>Ser<span>vices</span></h2>
  <ul class="arrow-list">
    <li>How do I find general information on women's health?</li>
    <li>What can I find information on living healthily?</li>
    <li>Where can I find answers to questions?</li>
    <li>What is Acupuncture? Where can I find more?</li>
    <li>Just for Fun</li>
    <li>How do I find general information on women's health?</li>
    <li>What can I find information on living healthily?</li>
    <li>Where can I find answers to questions?</li>
    <li>What is Acupuncture? Where can I find more?</li>
    <li>Just for Fun</li>
  </ul>
</section>
<div class="abs btn" style="left:868px;top:976px;width:60px">more info</div>

<section class="abs footer-col" style="left:115px;top:1013px">
  <h3>Navigate</h3>
  <ul><li>Home</li><li>About Us</li><li>Patient Information</li><li>Health</li><li>Pregnancy</li><li>Media</li><li>Locations</li></ul>
</section>
<div class="abs vrule" style="left:259px"></div>
<section class="abs footer-col" style="left:274px;top:1014px;width:192px">
  <h3>Hospital Affiliations</h3>
  <p>Dr. Qiu is a member of the medical staffs of Seabright Memorial Hospital and Palmvale Community Hospital. She is a member of the medical team at the Seabright Health Women's Health Center.</p>
</section>
<div class="abs vrule" style="left:487px"></div>
<section class="abs footer-col" style="left:515px;top:1021px;width:330px">
  <h3>Contact us</h3>
  <div class="contact-cols">
    <p>2240 Orchard Grove Ave<br>Suite 210-212<br>Marlow, Florida 33410<br>Tel: (555) 014-2290<br>Fax: (555) 014-2291</p>
    <p>875 Lantern Bay Road<br>Suite 104B<br>Palmvale, Florida 33470<br>Tel: (555) 017-3380<br>Fax: (555) 017-3381</p>
  </div>
</section>
<div class="abs badge" role="img" aria-label="Awareness month badge"><i></i></div>

<div class="abs legal" style="left:113px">(c) Copyright 2002, Lian-Hua Qiu, M.D., P.A, Website Powerd by Pixelgrove.</div>
<div class="abs legal" style="left:815px">© 2011 The Doctors of Coastline</div>
</body>
</html>
```